IT Freelancer (Consulting, trainer and project manager) needed letterhead

As a freelancer for IT Trainingswhip, consulting and project management I need a letterhead design. What is desired is a design that fits the existing logo (see Annex). It is functional, reliable, and equal time wirkenn Agil and modern. The whole is in color, as well as printed out to make a good impression on a black and white printer. The whole is to the existing Cooperate design (business card, homepage, logo) fit. Therefore, the choice of colors.

Target Market(s)

Customers such as medium-sized enterprises, training institutions

Industry/Entity Type

Consulting

Colors
0455a3
3277b5
85abd2
cfdfed
34a6d7
32a6d6
249fd4
0792cd
85cae6

Requirements
Must have
• Must include logo (see Annex) address (Ahornweg 14, 84317 Lindenau, Bavaria). Must seriously and act simultaneously Agil. Design should (even) be adaptable (signature, address, etc.) design must look good on a black / white laser

```html
<!DOCTYPE html>
<html lang="en">
<head>
<meta charset="utf-8">
<title>Lukas Brenner – Letterhead</title>
<link href="https://fonts.googleapis.com/css2?family=Source+Sans+3:wght@400;600;800&display=swap" rel="stylesheet">
<style>
  :root {
    --sky: #05aeef;
    --ocean: #1d75bc;
    --navy: #1d3f8c;
    --ink: #1a1a1a;
    --paper: #ffffff;
    --backdrop: #e4e4e4;
  }
  * { margin: 0; padding: 0; box-sizing: border-box; }
  html, body { width: 1116px; height: 1200px; overflow: hidden; background: var(--backdrop); }
  body { font-family: "Source Sans 3", Arial, sans-serif; color: var(--ink); }
  .letterhead {
    position: absolute; left: 93px; top: 0;
    width: 930px; height: 1200px;
    background: var(--paper); overflow: hidden;
  }
  .header-band, .footer-band { position: absolute; display: block; }
  .header-band { left: 0; top: 27px; width: 930px; height: 168px; }
  .footer-band { left: 0; bottom: 0; width: 930px; height: 50px; }
  .brand { position: absolute; left: 92px; top: 37px; width: 170px; text-align: center; }
  .brand-mark {
    width: 104px; height: 104px; border-radius: 50%;
    background: var(--navy); margin: 0 auto 18px;
    border: 3px solid var(--sky);
  }
  .brand-name {
    font-weight: 800; color: var(--navy);
    font-size: 25px; line-height: 25px; letter-spacing: 0.5px;
  }
  .contact { position: absolute; top: 132px; color: #fff; font-size: 14px; line-height: 21px; }
  .contact-col-a { left: 393px; }
  .contact-col-b { left: 564px; }
  .contact-item { display: flex; align-items: center; gap: 5px; white-space: nowrap; }
  .contact-item svg { width: 13px; height: 13px; flex: none; }
  .recipient { position: absolute; left: 123px; top: 335px; }
  .recipient-name { font-size: 18px; line-height: 22px; }
  .recipient-line { font-size: 12.5px; line-height: 16px; }
  .letter-body { position: absolute; left: 123px; top: 445px; width: 722px; }
  .letter-body p {
    font-size: 12.6px; line-height: 16.3px; text-align: justify;
    margin-bottom: 33px; hyphens: auto;
  }
  .closing { position: absolute; left: 123px; top: 957px; }
  .closing-word { font-size: 12.5px; line-height: 16px; }
  .closing-name { font-size: 21px; line-height: 26px; }
</style>
</head>
<body>
<main class="letterhead">
  <svg class="header-band" viewBox="0 0 930 168" aria-hidden="true">
    <polygon points="287,0 930,0 930,168 329,168" fill="var(--ocean)"/>
    <polygon points="305,0 930,0 930,168 346,168" fill="var(--sky)"/>
  </svg>

  <div class="brand">
    <div class="brand-mark"></div>
    <div class="brand-name">LUKAS<br>BRENNER</div>
  </div>

  <div class="contact contact-col-a">
    <div class="contact-item">
      <svg viewBox="0 0 16 16"><circle cx="8" cy="8" r="7" fill="none" stroke="#fff" stroke-width="1.2"/><path d="M5.5 4.5l1.5 1.5-1 1c.6 1.3 1.5 2.2 2.8 2.8l1-1 1.5 1.5-1.2 1.2C7.5 11.2 4.8 8.5 4.3 5.7z" fill="#fff"/></svg>
      <span>88-456-210378</span>
    </div>
    <div class="contact-item">
      <svg viewBox="0 0 16 16"><circle cx="8" cy="8" r="7" fill="none" stroke="#fff" stroke-width="1.2"/><rect x="4" y="5.5" width="8" height="5.5" fill="none" stroke="#fff"/><path d="M4 5.5l4 3 4-3" fill="none" stroke="#fff"/></svg>
      <span>kontakt@brenner-it.de</span>
    </div>
  </div>

  <div class="contact contact-col-b">
    <div class="contact-item">
      <svg viewBox="0 0 16 16" fill="none" stroke="#fff" stroke-width="1"><circle cx="8" cy="8" r="6.5"/><ellipse cx="8" cy="8" rx="3" ry="6.5"/><path d="M1.5 8h13M2.5 5h11M2.5 11h11"/></svg>
      <span>www.brenner-it.de</span>
    </div>
    <div class="contact-item">
      <svg viewBox="0 0 16 16"><circle cx="8" cy="8" r="7" fill="none" stroke="#fff" stroke-width="1.2"/><path d="M8 3.8L3.8 7.6h1.3v4.4h2.1V9.5h1.6V12h2.1V7.6h1.3z" fill="#fff"/></svg>
      <span>Ahornweg 14, 84317 Lindenau, Bavaria</span>
    </div>
  </div>

  <section class="recipient">
    <div class="recipient-name">Mr. Peter Hallmann</div>
    <div class="recipient-line">Managing Director</div>
    <div class="recipient-line">Northfield Business Center</div>
  </section>

  <section class="letter-body">
    <p>Maecenas non rutrum libero. Donec odio lorem, vehicula eu fermentum ut, varius vel purus. Sed varius faucibus enim eu tincidunt. Nullam accumsan metus elit, et blandit risus tincidunt id. Etiam laoreet ultricies est, eu venenatis orci pharetra quis. Cras ut efficitur massa. Mauris nec sodales libero, id pretium quam. Mauris et nulla nec nunc imperdiet ultricies. Sed suscipit, felis eget dignissim luctus, erat nisl euismod nibh, in dignissim nisl est et neque. Proin bibendum quis felis id dignissim. Nulla vitae elementum neque. Nam sollicitudin felis dui, quis consectetur elit accumsan a. Maecenas eget erat eleifend, fermentum metus vel, mattis nunc. Duis at rutrum ligula, sit amet finibus arcu. Aliquam lacus nulla, molestie id porta gravida, rutrum molestie nisi. Proin volutpat nisl ac pharetra dictum. Curabitur sed quam ex. Ut pellentesque pulvinar purus, at sagittis arcu porttitor eu. Nam suscipit vestibulum blandit. Ut tempus ante sed arcu sollicitudin, non hendrerit sem porttitor. In congue in justo ut vehicula. Sed pellentesque felis ut velit placerat, ut tristique massa vestibulum. Integer viverra, massa eget scelerisque tempus, magna quam convallis nibh, vel consectetur turpis diam vitae nisl. Donec lobortis placerat dolor.</p>
    <p>Nullam accumsan metus elit, et blandit risus tincidunt id. Etiam laoreet ultricies est, eu venenatis orci pharetra quis. Cras ut efficitur massa. Mauris nec sodales libero, id pretium quam. Mauris et nulla nec nunc imperdiet ultricies. Sed suscipit, felis eget dignissim luctus, erat nisl euismod nibh, in dignissim nisl est et neque. Proin bibendum quis felis id dignissim. Nulla vitae elementum neque. Nam sollicitudin felis dui, quis consectetur elit accumsan a. Maecenas eget erat eleifend, fermentum metus vel, mattis nunc. Duis at rutrum ligula, sit amet finibus arcu. Aliquam lacus nulla, molestie id porta gravida, rutrum molestie nisi. Proin volutpat nisl ac pharetra dictum. Curabitur sed quam ex accumsan eget erat.</p>
    <p>Nullam accumsan metus elit, et blandit risus tincidunt id. Etiam laoreet ultricies est, eu venenatis orci pharetra quis. Cras ut efficitur massa. Mauris nec sodales libero, id pretium quam. Mauris et nulla nec nunc imperdiet ultricies. Sed suscipit, felis eget dignissim luctus, erat nisl euismod nibh, in dignissim nisl est et neque. Proin bibendum quis felis id dignissim. Nulla vitae elementum neque. Nam sollicitudin felis dui, quis consectetur elit accumsan.</p>
  </section>

  <section class="closing">
    <div class="closing-word">Sincerely</div>
    <div class="closing-name">Tomas Reiner</div>
  </section>

  <svg class="footer-band" viewBox="0 0 930 50" aria-hidden="true">
    <polygon points="0,0 604,0 616,50 0,50" fill="var(--ocean)"/>
    <polygon points="0,0 587,0 598,50 0,50" fill="var(--sky)"/>
  </svg>
</main>
</body>
</html>
```